Homepage redesign - Varrek Motorcycle importer

Hi Designers, This is my first project so apologies for any mistakes I have made and any missed information, that is why i have allowed 15 days for the design project.
We are an independant motorcycle importer & are currently selling our "Product" a re-designed motorcycle as a Fast-food delivery motorcycle.The brand VARREK is relatively new to the UK however we have been supplying VARREK bikes for the past 6 years, problem our website :
www.ridequill.co.uk is very dated/ looks bland & has a very amateur feel to it. We require a complete "Homepage re-design" only. The design will then be used as a base for the remaining other pages..which we will sort.

All our customers are UK London based it would be good to see "Design features" associated with this location if possible- Good luck!

Target Market(s)

Primarily our website will be targeted to owners & operaters of "Fast-food stores" ie Tabberly`s Pizza, Mama Fenns etc...However we would still like to retain an image of the standard bike as well, unmodified so that the normal non commercial customer may see their future purchase.Generally males of various nationality between the ages of 25 to 50 are the target.

Industry/Entity Type

Delivery

Requirements
Must have
• Should use the "Varrek" logo supplied or a "Varrek" logo from elsewhere. Consideration must be made somewhere to show the amount of stock/ spares we carry either via text/image or both that is available online 24/7 off the shelf to back up their purchase for next day delivery..Very Important, When a bike is down they are losing money.
• Banner or emblem stating "1 Year full warranty" Guarrantee. "Ridequill.co.uk" should be part of the design somewhere within the page.
Nice to have
• Possibly links/styles associated to that of Fast-food shops, not essential just a thought. Maybe some animation but not too much that it looks tacky/cheap.
• We are associated with this company and therefore the feel of the homepage should be at least comparable as evetually there will be a recripricle link :
• http://www.plumwhistle.uk.com/
• Our target customers are these people:
• http://www.tabberlys.example/home/index.jsp
• http://www.mamafenns.example/index.shtm
• Light Competition possibly these, however wrong country:
• http://www.quoltrax.example/delivery.htm
• Consideration: All of our bikes we sell are Blue as shown in the images the only other colour we may possible sell would be red. Just in case this helps with the styles/ graphics etc that you have in mind.
• Would like a "Contact us" one that allows enquiry`s to be sent direct from that page also in doing this it will give us there contact email ideal for future direct marketing...very important.
Should not have
• No obvious copying of other sites just an amalgamation of site ideas to create something very original if poss.
• None of these images on the existing homepage are current so therefore I will load up some however please let me know what further images are required ....

```html
<!DOCTYPE html>
<html lang="en">
<head>
<meta charset="utf-8">
<title>Ridequill.co.uk – Varrek Motorcycles</title>
<link rel="stylesheet" href="https://fonts.googleapis.com/css2?family=Arimo:wght@400;700&family=Oswald:wght@500;700&family=Ubuntu:wght@400;700&display=swap">
<style>
:root{
  --red:#c4161c;
  --red-dark:#8e0c10;
  --blue:#2b8fd6;
  --blue-dark:#13508f;
  --panel:#3c3b3b;
  --banner:#2a2a2a;
  --ink:#333;
  --soft:#e2e2e2;
  --strip:#ececec;
  --white:#fff;
}
*{box-sizing:border-box;margin:0;padding:0}
html,body{width:1169px;height:1200px;overflow:hidden;background:var(--white)}
body{font-family:"Arimo",Arial,sans-serif;color:var(--ink)}
.stage{position:absolute;left:0;top:0;width:1280px;height:1314px;transform:scale(.9133);transform-origin:0 0;
  background:linear-gradient(#262626 0,#5a5a5a 200px,#dcdcdc 420px,#fff 480px)}
.abs{position:absolute}

/* navigation */
.nav a{position:absolute;top:30px;height:33px;border-radius:7px;color:#fff;font-size:12px;text-decoration:none;
  display:flex;align-items:center;justify-content:center;
  background:linear-gradient(#d8262c,var(--red-dark));box-shadow:0 2px 3px rgba(0,0,0,.5)}
.nav a.active{background:linear-gradient(#5fb5ee,var(--blue-dark))}

/* banner */
.banner{left:146px;top:90px;width:988px;height:384px;border-radius:18px;background:linear-gradient(#3a3a3a,#1c1c1c)}
.tab{left:166px;top:78px;width:420px;height:316px;border-radius:0 0 16px 16px;background:linear-gradient(#4a4949,var(--panel));box-shadow:0 3px 6px rgba(0,0,0,.5)}
.hanger{left:340px;top:380px;width:63px;height:84px;border-radius:0 0 14px 14px;background:var(--panel)}
.hanger i{position:absolute;left:20px;top:52px;width:19px;height:19px;border-radius:50%;background:#1e1e1e}
.plate{left:282px;top:122px;width:185px;height:128px;border-radius:3px;background:linear-gradient(#e4e4e4,#8d8d8d);
  box-shadow:0 4px 10px rgba(0,0,0,.6);display:flex;align-items:center;justify-content:center;gap:8px}
.plate .dot{width:16px;height:16px;border-radius:50%;background:var(--red)}
.plate .name{font-family:"Ubuntu",sans-serif;font-weight:700;font-size:26px;color:var(--red)}
.model{left:212px;top:278px;color:#eee;font-family:"Ubuntu",sans-serif;font-size:24px}
.model b{font-weight:700}
.price{left:213px;color:#ddd;font-size:12px}
.price b{color:#fff}
.delivery{left:212px;top:350px;color:#fff;font-size:12px;font-weight:700}
.tag{left:422px;top:403px;width:140px;height:42px;border-radius:8px;background:linear-gradient(#d42027,var(--red-dark));
  transform:rotate(-12deg);color:#fff;font-size:12px;font-weight:700;display:flex;align-items:center;justify-content:center;letter-spacing:.5px;box-shadow:0 3px 5px rgba(0,0,0,.5)}
.photo{left:596px;top:98px;width:530px;height:328px;border-radius:14px;border:1px solid #444;
  background:radial-gradient(ellipse at 55% 50%,#2a4fb5 0,#1e2d6a 22%,#141414 48%,#000 100%)}
.dots span{position:absolute;top:439px;width:23px;height:23px;border-radius:50%;background:#5f5f5f;color:#ddd;font-size:11px;
  display:flex;align-items:center;justify-content:center}
.dots span.on{width:28px;height:28px;top:436px;background:var(--red);color:#fff}

/* feature strip */
.strip{left:146px;top:494px;width:988px;height:152px;border-radius:16px;border:1px solid #ccc;background:linear-gradient(#fafafa,var(--strip) 55%,#dcdcdc)}
.card{position:absolute;top:521px;height:98px;border-radius:12px;color:#fff;box-shadow:0 3px 6px rgba(0,0,0,.35)}
.card.blue{background:linear-gradient(#4aa5e8,var(--blue) 55%,var(--blue-dark))}
.card.red{background:linear-gradient(#ee5c5f,#d0282e 55%,var(--red-dark))}
.card .big{position:absolute;font-family:"Oswald",sans-serif;font-weight:700;font-size:31px;text-shadow:0 2px 2px rgba(0,0,0,.4)}
.card .sub{position:absolute;font-family:"Ubuntu",sans-serif;font-size:19px}
.rosette{position:absolute;left:20px;top:12px;width:80px;height:80px;border-radius:50%;background:radial-gradient(#fff 0,#fff 30%,#c92a31 32%,#9b1419 100%)}
.clock{position:absolute;left:8px;top:8px;width:82px;height:82px;border-radius:50%;background:rgba(0,30,70,.35)}
.rider{position:absolute;right:8px;top:6px;width:80px;height:84px;border-radius:50%;background:rgba(60,0,0,.35)}
.card .brand{position:absolute;left:20px;top:12px;font-family:"Ubuntu",sans-serif;font-weight:700;font-size:28px}
.card .line{position:absolute;left:18px;font-family:"Ubuntu",sans-serif;font-size:12px}
.msg{text-align:center;font-size:12px}

/* content */
h2{position:absolute;left:163px;color:var(--red);font-size:13.5px;font-weight:700}
.copy{position:absolute;font-size:12px;line-height:14.5px;color:#333}
.more{left:781px;top:762px;font-size:12px;color:var(--red)}
.rule{left:163px;top:785px;width:705px;height:1px;background:#ccc}
.bullets{position:absolute;list-style:none;font-size:12px;line-height:14.5px;color:#333}
.bullets li{position:relative;padding-left:14px;margin-bottom:14.5px}
.bullets li::before{content:"";position:absolute;left:-1px;top:4px;width:6px;height:6px;border-radius:50%;background:var(--red)}

/* payments */
.pay{left:891px;top:667px;width:243px;height:191px;border-radius:16px;border:1px solid #ccc;background:linear-gradient(#fff,#e6e6e6)}
.pay h3{position:absolute;left:18px;top:28px;font-size:12px;color:var(--red)}
.chip{position:absolute;height:30px;border-radius:3px;color:#fff;font-size:10px;font-weight:700;display:flex;align-items:center;justify-content:center}

/* footer */
.footer{left:146px;top:1028px;width:987px;height:199px;border-radius:18px;background:var(--soft)}
.contact{left:175px;top:1044px;font-size:10.5px;line-height:13.3px;color:#333}
.contact b{display:block;margin-bottom:6px;font-size:11px}
.follow{left:959px;top:1099px;font-size:10.5px;font-weight:700;color:#444}
.social span{position:absolute;top:1115px;width:31px;height:31px;border-radius:6px;color:#fff;font-size:8px;font-weight:700;display:flex;align-items:center;justify-content:center}
.copyright{left:0;width:1280px;top:1243px;text-align:center;font-size:10.5px;color:#333}
</style>
</head>
<body>
<div class="stage">

  <nav class="nav">
    <a class="active" style="left:609px;width:86px">Home</a>
    <a style="left:704px;width:86px">About us</a>
    <a style="left:799px;width:86px">Contact us</a>
    <a style="left:894px;width:86px">Products</a>
    <a style="left:989px;width:124px">Term &amp; Conditions</a>
  </nav>

  <section class="abs banner"></section>
  <div class="abs hanger"><i></i></div>
  <div class="abs tab"></div>
  <div class="abs plate"><span class="dot"></span><span class="name">VARREK</span></div>
  <div class="abs model"><b>VX110 - 3R11</b> MOTORCYCLES</div>
  <div class="abs price" style="top:311px"><b>£999</b>&nbsp; Full Assembled As Per Picture, Taxed, Number.</div>
  <div class="abs price" style="top:327px"><b>£899</b>&nbsp; Full Assembled Without Racks. Taxed, Number Plates.</div>
  <div class="abs delivery">ALL PRICES INC. FREE U.K. DELIVERY.</div>
  <div class="abs tag">RIDEQUILL.CO.UK</div>
  <div class="abs photo" role="img" aria-label="Photo of a blue Varrek delivery motorcycle with a blue top box"></div>
  <div class="dots">
    <span class="on" style="left:773px">1</span>
    <span style="left:813px">2</span><span style="left:844px">3</span><span style="left:875px">4</span>
    <span style="left:906px">5</span><span style="left:937px">6</span>
  </div>

  <section class="abs strip"></section>
  <div class="card blue" style="left:177px;width:243px">
    <div class="rosette" role="img" aria-label="Red guarantee rosette emblem"></div>
    <div class="big" style="left:141px;top:14px">1 YEAR</div>
    <div class="sub" style="left:107px;top:65px">full warranty</div>
  </div>
  <div class="card blue" style="left:452px;width:243px">
    <div class="clock" role="img" aria-label="Clock illustration"></div>
    <div class="big" style="left:40px;top:14px">24/7 Available</div>
    <div class="sub" style="left:85px;top:66px;font-size:18px">STOCK / SPARES</div>
  </div>
  <div class="card red" style="left:728px;width:243px">
    <div class="rider" role="img" aria-label="Illustration of a rider on a motorbike"></div>
    <div class="brand">Ridesure</div>
    <div class="line" style="top:63px">YOUR ONE STOP</div>
    <div class="line" style="top:77px">FOR ONLINE BIKE INSURANCE</div>
  </div>
  <div class="card red msg" style="left:1001px;width:101px">
    <div style="position:absolute;left:0;right:0;top:21px;font-weight:700;line-height:14px">MESSAGE<br>BOX</div>
    <div style="position:absolute;left:0;right:0;top:69px">Click Here</div>
  </div>

  <h2 style="top:674px">Welcome</h2>
  <p class="copy" style="left:163px;top:694px;width:710px">Ridequill.co.uk is absolutely dedicated to your total satisfaction, now and in the future. Our aim is to provide you the customer with a brand new motorcycle either pre-registered (which can be despatched the next day) or one which Registration Requires my Name/Address, at the best possible prices ever.</p>
  <p class="copy" style="left:163px;top:751px">All this from the comfort of your own home.</p>
  <div class="abs more">&gt;&gt;Read more...</div>
  <div class="abs rule"></div>

  <h2 style="top:805px">Product Details:</h2>
  <ul class="bullets" style="left:163px;top:835px;width:290px">
    <li>Powered by 107 cc capacity four stroke engine for reliability, efficiency and easily maintained.</li>
    <li>Fuel consumption, 120 M.P.G achieved at realis-tic speeds between 40 and 60 M.P.H</li>
    <li>Four-Speed semi-automatic cyclonic gearbox. When at standstill can change from 4th gear to neutral with one forward press on the gear selector. Ideal for town work.</li>
    <li>Electric and kick starter operation.</li>
  </ul>
  <ul class="bullets" style="left:494px;top:835px;width:360px">
    <li>Disc front and rear brakes.</li>
    <li>Speedometer reads in KMH and MPH.</li>
    <li>Fuel gauge.</li>
    <li>Indicated gear read out display on the dash.</li>
  </ul>

  <aside class="abs pay">
    <h3>Payment Options:</h3>
    <span class="chip" style="left:18px;top:53px;width:29px;background:#8e3b8f">Pelo</span>
    <span class="chip" style="left:50px;top:53px;width:29px;background:#15794a">Strand</span>
    <span class="chip" style="left:82px;top:53px;width:29px;background:#2d5ea8">Kiro</span>
    <span class="chip" style="left:115px;top:53px;width:56px;background:#333;border-radius:15px">Evo</span>
    <span class="chip" style="left:18px;top:97px;width:50px;background:#1a4fa0">Vessa</span>
    <span class="chip" style="left:71px;top:97px;width:50px;background:#1d3f8f">Dunlin</span>
    <span class="chip" style="left:123px;top:97px;width:50px;background:#1a5fb0">Vessa Plus</span>
    <span class="chip" style="left:176px;top:97px;width:48px;background:#d8412a">Merrow</span>
    <span class="chip" style="left:18px;top:135px;width:50px;background:#1b5fae">Ostra</span>
    <span class="abs" style="left:72px;top:142px;font-size:14px;font-weight:700;color:#1d3f7a">Paygrove</span>
  </aside>

  <footer class="abs footer"></footer>
  <div class="abs contact">
    <b>CONTACT US:</b>
    K.T.Imports.<br>12 Harrowfield Lane,<br>Oakbridge,<br>Marlow Vale,<br>MV4 7QT.<br><br>
    Tel: 01632 960418<br>Mob: 07700 900562<br>Fax: 01632 960418<br><br>
    Email : Sales@ridequill.co.uk
  </div>
  <div class="abs follow">Follow us on:</div>
  <div class="social">
    <span style="left:958px;background:#3fb1e0">Chirpa</span>
    <span style="left:996px;background:#3b5ea6">Facets</span>
    <span style="left:1034px;background:#1b7ab8">Linkly</span>
    <span style="left:1073px;background:#ec7420">Feedo</span>
  </div>
  <div class="abs copyright">Copyright © Ridequill.co.uk. 2005</div>

</div>
</body>
</html>
```